Brightpath Coverage Partners
Stationary
Project: Brightpath Coverage Partners
Brightpath Coverage Partners -
Creative Brief
Professional
Dorian Fell
Agent / Broker
71362 West Maple Lane Ste. B Idyllwild, CA 92871-0517
dorian@brightpathcoverage.example
www.brightpathcoverage.example
Insurance License No: 0K72918
Please put the main lines of insurance I sell: Home, Auto, Commercial, Life, Health, Retirement

```html
<!DOCTYPE html>
<html lang="en">
<head>
<meta charset="utf-8">
<title>Brightpath Coverage Partners — Stationery</title>
<link href="https://fonts.googleapis.com/css2?family=Questrial&display=swap" rel="stylesheet">
<style>
:root{
  --bg:#e9e6e1;
  --paper:#ffffff;
  --navy:#0d2a5c;
  --blue:#1f4f9c;
  --sky:#5d86c8;
  --ink:#2b2b2b;
  --muted:#7a7a7a;
  --rule:#b9b9b9;
}
*{box-sizing:border-box;margin:0;padding:0}
html,body{width:1200px;height:554px;overflow:hidden;background:var(--bg);font-family:"Questrial",sans-serif;color:var(--ink)}
.canvas{position:relative;width:1200px;height:554px}
.sheet,.card,.envelope{position:absolute;background:var(--paper);box-shadow:0 2px 6px rgba(0,0,0,.18);overflow:hidden}
.sheet{top:36px;width:380px;height:497px}
.sheet--one{left:20px}
.sheet--two{left:414px}
.swoosh{position:absolute;right:0;bottom:0}
.brand{position:absolute;display:flex;align-items:center;gap:5px;color:var(--navy);font-size:11px;line-height:1.1}
.brand-mark{width:12px;height:12px;background:var(--blue);flex:none}
.sheet .brand{right:22px;top:52px;width:120px}
.services{position:absolute;right:22px;top:86px;font-size:6px;color:var(--navy);border-top:1px solid var(--blue);padding-top:3px;letter-spacing:.2px}
.fax-title{position:absolute;left:26px;top:146px;font-size:22px;color:var(--ink)}
.fields{position:absolute;left:26px;right:26px;top:188px;display:grid;grid-template-columns:1fr 1fr;column-gap:14px;row-gap:11px}
.sheet--two .fields{grid-template-columns:1fr 1fr}
.field{display:flex;font-size:6px;color:var(--muted);border-bottom:1px solid var(--rule);padding-bottom:2px}
.checks{position:absolute;left:26px;right:26px;top:318px;display:flex;justify-content:space-between}
.check{display:flex;align-items:center;gap:4px;font-size:6px;color:var(--muted)}
.check::before{content:"";width:7px;height:7px;border:1px solid var(--muted)}
.footer{position:absolute;left:26px;bottom:26px;display:flex;gap:26px;font-size:5px;color:var(--muted);line-height:1.5}
.card{top:36px;height:113px}
.card--front{left:816px;width:188px}
.card--back{left:1016px;width:162px}
.person{position:absolute;left:10px;top:10px;font-size:7px;color:var(--navy);line-height:1.4}
.person .role{font-size:5px;color:var(--muted)}
.card--front .brand{right:10px;top:14px;width:80px;font-size:7.5px}
.card-contact{position:absolute;left:10px;top:52px;font-size:4.5px;color:var(--muted);line-height:1.5}
.card--back .brand{left:36px;top:18px;width:100px;font-size:8px}
.card--back .services{left:34px;right:auto;top:44px;font-size:4px}
.envelope{left:816px;top:174px;width:362px;height:366px}
.envelope .brand{left:14px;top:18px;width:110px;font-size:10px}
.env-address{position:absolute;left:14px;top:64px;font-size:5px;color:var(--muted);line-height:1.5}
.env-window{position:absolute;right:22px;top:50px;width:130px;height:52px;border:1px solid var(--rule);border-radius:3px}
.env-band{position:absolute;left:0;bottom:0}
.env-web{position:absolute;right:28px;top:189px;font-size:7px;color:var(--paper);letter-spacing:.3px}
.env-services{position:absolute;left:140px;top:160px;font-size:6px;color:var(--navy)}
</style>
</head>
<body>
<main class="canvas">

  <section class="sheet sheet--one" aria-label="Fax cover sheet">
    <div class="brand"><span class="brand-mark"></span><span>Brightpath Coverage Partners</span></div>
    <p class="services">Home | Auto | Commercial | Life | Health | Retirement</p>
    <h1 class="fax-title">FAX</h1>
    <div class="fields">
      <span class="field">To:</span><span class="field">From:</span>
      <span class="field">Fax:</span><span class="field">Pages:</span>
      <span class="field">Phone:</span><span class="field">Date:</span>
      <span class="field">Re:</span><span class="field">CC:</span>
    </div>
    <div class="checks">
      <span class="check">Urgent</span><span class="check">For Review</span><span class="check">Please Comment</span><span class="check">Please Reply</span><span class="check">Please Recycle</span>
    </div>
    <div class="footer">
      <p>71362 West Maple Lane Ste. B<br>Idyllwild, CA 92871-0517</p>
      <p>Ph: 951 555 0142<br>Fax: 951 555 0143</p>
      <p>dorian@brightpathcoverage.example<br>www.brightpathcoverage.example</p>
    </div>
    <svg class="swoosh" width="170" height="110" viewBox="0 0 170 110">
      <defs><linearGradient id="sw1" x1="0" y1="0" x2="1" y2="1"><stop offset="0" stop-color="#5d86c8"/><stop offset="1" stop-color="#0d2a5c"/></linearGradient></defs>
      <path d="M170 0 C150 55 95 95 0 110 L170 110 Z" fill="url(#sw1)"/>
      <path d="M170 18 C150 66 110 96 40 110" stroke="#fff" stroke-width="2" fill="none" opacity=".7"/>
    </svg>
  </section>

  <section class="sheet sheet--two" aria-label="Fax cover sheet, alternate">
    <div class="brand"><span class="brand-mark"></span><span>Brightpath Coverage Partners</span></div>
    <p class="services">Home | Auto | Commercial | Life | Health | Retirement</p>
    <h1 class="fax-title">FAX</h1>
    <div class="fields">
      <span class="field">To:</span><span class="field">From:</span>
      <span class="field">Fax:</span><span class="field">Pages:</span>
      <span class="field">Phone:</span><span class="field">Date:</span>
      <span class="field">Re:</span><span class="field">CC:</span>
    </div>
    <div class="checks">
      <span class="check">Urgent</span><span class="check">For Review</span><span class="check">Please Comment</span><span class="check">Please Reply</span><span class="check">Please Recycle</span>
    </div>
    <div class="footer">
      <p>71362 West Maple Lane Ste. B<br>Idyllwild, CA 92871-0517</p>
      <p>Ph: 951 555 0142<br>Fax: 951 555 0143</p>
      <p>dorian@brightpathcoverage.example<br>www.brightpathcoverage.example</p>
    </div>
    <svg class="swoosh" width="170" height="90" viewBox="0 0 170 90">
      <path d="M170 0 C150 45 95 78 0 90 L170 90 Z" fill="url(#sw1)"/>
    </svg>
  </section>

  <section class="card card--front" aria-label="Business card front">
    <div class="person">Dorian Fell<br><span class="role">Agent / Broker</span></div>
    <div class="brand"><span class="brand-mark"></span><span>Brightpath Coverage Partners</span></div>
    <div class="card-contact">
      71362 West Maple Lane Ste. B<br>Idyllwild, CA 92871-0517<br>Ph: 951 555 0142<br>dorian@brightpathcoverage.example<br>Insurance License No: 0K72918
    </div>
    <svg class="swoosh" width="110" height="60" viewBox="0 0 110 60">
      <path d="M110 0 C100 30 65 52 0 60 L110 60 Z" fill="url(#sw1)"/>
    </svg>
  </section>

  <section class="card card--back" aria-label="Business card back">
    <div class="brand"><span class="brand-mark"></span><span>Brightpath Coverage Partners</span></div>
    <p class="services">Home | Auto | Commercial | Life | Health | Retirement</p>
    <svg class="swoosh" width="162" height="50" viewBox="0 0 162 50">
      <path d="M162 0 C130 28 70 44 0 36 L0 50 L162 50 Z" fill="url(#sw1)"/>
    </svg>
  </section>

  <section class="envelope" aria-label="Envelope">
    <div class="brand"><span class="brand-mark"></span><span>Brightpath Coverage Partners</span></div>
    <div class="env-address">71362 West Maple Lane Ste. B<br>Idyllwild, CA 92871-0517<br>Ph: 951 555 0142</div>
    <div class="env-window"></div>
    <p class="env-services">Home | Auto | Commercial | Life | Health | Retirement</p>
    <svg class="env-band" width="362" height="200" viewBox="0 0 362 200">
      <defs><linearGradient id="sw2" x1="0" y1="0" x2="0" y2="1"><stop offset="0" stop-color="#1f4f9c"/><stop offset="1" stop-color="#0d2a5c"/></linearGradient></defs>
      <path d="M0 0 L362 0 L362 36 C280 28 220 30 180 70 C140 30 80 28 0 36 Z" fill="none"/>
      <path d="M0 0 L362 0 L362 40 L181 84 L0 40 Z" fill="url(#sw2)"/>
      <path d="M0 40 L181 84 L362 40" stroke="#5d86c8" stroke-width="2" fill="none"/>
    </svg>
    <p class="env-web">www.brightpathcoverage.example</p>
  </section>

</main>
</body>
</html>
```